Billboard design - consider what a billboard is

Design a billboard using my logo - Billboard is 6m x 3m
A Billboard is advertising for my company that is on a big sign.

Has to be clean and easy to read, and ideally highlights that we are Residential and Commercial builders.

Keep it clean and easy to read

The contact number for the board is

022 583 7092
www.harbourframeworks.co.nz
info@harbourframeworks.co.nz

Doesnt have to have all contact details if it doesnt fit

Has to catch peoples attention to contact us if they need a builder

Can you please change the sign to be all white writing, with black background ?
Updates

Please consider what a billboard is...

The design needs to be suitable for a billboard..

Target Market(s)

people driving past

Industry/Entity Type

Construction

Logo Text

Wellington Builder, website email address, contact number

Colors
0054AA
0677BA
7BADD7
CADEEF
E8F1F8

Requirements
Must have
• Easy to read
Nice to have
• easy to read, can clearly see contact details

```html
<!DOCTYPE html>
<html lang="en">
<head>
<meta charset="utf-8">
<title>Harbour Frameworks – Billboard</title>
<link rel="stylesheet" href="https://fonts.googleapis.com/css2?family=Quicksand:wght@600;700&display=swap">
<style>
  :root {
    --board-black: #000000;
    --text-white: #ffffff;
    --accent-blue: #0677ba;
    --accent-deep: #0054aa;
    --accent-light: #7badd7;
  }
  * { margin: 0; padding: 0; box-sizing: border-box; }
  html, body {
    width: 1200px;
    height: 619px;
    overflow: hidden;
    background: var(--board-black);
  }
  .billboard {
    position: relative;
    width: 1200px;
    height: 619px;
    overflow: hidden;
    background: var(--board-black);
    font-family: "Quicksand", sans-serif;
    color: var(--text-white);
  }
  .billboard__shapes {
    position: absolute;
    inset: 0;
  }
  .brand {
    position: absolute;
    left: 96px;
    top: 110px;
    width: 620px;
  }
  .brand__name {
    font-weight: 700;
    font-size: 104px;
    line-height: 0.98;
    letter-spacing: -2px;
  }
  .brand__services {
    margin-top: 10px;
    font-weight: 700;
    font-size: 30px;
    line-height: 36px;
    letter-spacing: 1px;
    color: var(--accent-light);
  }
  .contact {
    position: absolute;
    left: 500px;
    top: 408px;
    width: 696px;
    text-align: center;
    font-weight: 700;
  }
  .contact__phone {
    font-size: 46px;
    line-height: 58px;
    letter-spacing: 1px;
  }
  .contact__web,
  .contact__email {
    font-size: 32px;
    line-height: 42px;
    letter-spacing: 0.5px;
  }
</style>
</head>
<body>
  <main class="billboard">
    <svg class="billboard__shapes" width="1200" height="619" viewBox="0 0 1200 619" aria-hidden="true">
      <circle class="accent-circle accent-circle--top" cx="972" cy="110" r="265" fill="var(--accent-blue)"/>
      <circle class="accent-circle accent-circle--bottom" cx="215" cy="700" r="325" fill="var(--accent-deep)"/>
    </svg>

    <header class="brand">
      <h1 class="brand__name">Harbour<br>Frameworks</h1>
      <p class="brand__services">Residential &amp; Commercial Builders</p>
    </header>

    <section class="contact">
      <p class="contact__phone">022 583 7092</p>
      <p class="contact__web">www.harbourframeworks.co.nz</p>
      <p class="contact__email">info@harbourframeworks.co.nz</p>
    </section>
  </main>
</body>
</html>
```